Bolen's New Year Party

The following text with a New Year's Holiday Theme

The Soiree Foundry presents:
Bolen’s 3rd Annual New Year’s Eve Party

Location Costaluz 72B
Date Dec 31st starting at 10pm
DJ Inside
Live Band Outside
Food
Beverages
Bounce House
King of Pearls Champagne

Raffle tickets will be sold for a 20.00 donation at location or contact 63928/19476
1st Prize 46 inch Vextra LED TV
2nd Prize 100 dollar Gift Certificate
3rd Prize 50 dollar Gift Certificate
Drawing starts at 1:30 AM

```html
<!DOCTYPE html>
<html lang="en">
<head>
<meta charset="utf-8">
<title>Bolen's 3rd Annual New Years Eve Party</title>
<link rel="stylesheet" href="https://fonts.googleapis.com/css2?family=Open+Sans:wght@400;600;700&family=Montserrat:wght@700;800&display=swap">
<style>
  :root {
    --bg-red: #ee2e2e;
    --glow-dark: rgba(90, 0, 0, 0.55);
    --date-top: #b87486;
    --date-bottom: #8c3f60;
    --ink-white: #ffffff;
    --ink-dark: #1a1a1a;
    --silver-light: #ffffff;
    --silver-mid: #d9d9d9;
    --silver-dark: #8d8d8d;
    --gold-light: #fff25a;
    --gold-dark: #e9b800;
    --lime: #b7d63a;
    --prize-blue: #2456a0;
    --first-gold: #ffe11a;
    --second-silver: #c9ced8;
    --third-bronze: #7d6a3a;
  }
  * { margin: 0; padding: 0; box-sizing: border-box; }
  html, body { width: 1200px; height: 900px; overflow: hidden; }
  body { background: var(--bg-red); font-family: "Open Sans", Arial, sans-serif; color: var(--ink-white); }
  .flyer { position: relative; width: 1200px; height: 900px; overflow: hidden; background: var(--bg-red); }
  .center { position: absolute; left: 0; width: 1160px; text-align: center; white-space: nowrap; }

  .date-banner {
    position: absolute; left: 316px; top: 44px; width: 540px; height: 98px;
    background: linear-gradient(var(--date-top), var(--date-bottom));
    text-align: center; padding-top: 12px; white-space: nowrap;
  }
  .date-banner .date { font-family: "Montserrat", Arial, sans-serif; font-weight: 800; font-size: 37px; line-height: 38px; letter-spacing: 1px; }
  .date-banner .venue { font-size: 36px; line-height: 40px; letter-spacing: 0.5px; }

  .title-glow {
    position: absolute; left: 320px; top: 230px; width: 540px; height: 260px;
    background: radial-gradient(ellipse at center, var(--glow-dark), rgba(90,0,0,0) 70%);
  }
  .presenter { top: 176px; font-size: 25px; line-height: 34px; color: var(--ink-dark); letter-spacing: 0.5px; }
  .headline {
    top: 196px; font-family: "Open Sans", Arial, sans-serif; font-weight: 600; font-size: 124px; line-height: 140px;
    letter-spacing: 1px;
  }
  .headline span {
    background: linear-gradient(var(--silver-light) 20%, var(--silver-mid) 55%, var(--silver-dark));
    -webkit-background-clip: text; background-clip: text; color: transparent;
    filter: drop-shadow(3px 3px 0 #333) drop-shadow(0 6px 8px rgba(0,0,0,0.4));
  }
  .annual {
    top: 320px; font-family: "Montserrat", Arial, sans-serif; font-weight: 800; font-size: 71px; line-height: 76px;
  }
  .annual span {
    background: linear-gradient(var(--gold-light), var(--gold-dark));
    -webkit-background-clip: text; background-clip: text; color: transparent;
    filter: drop-shadow(2px 3px 0 #5a3a00);
  }
  .party-name { top: 384px; font-size: 46px; line-height: 52px; color: var(--lime); text-shadow: 1px 2px 0 #4a5a10; }
  .party-reflection {
    top: 426px; font-size: 46px; line-height: 52px; color: var(--lime); transform: scaleY(-1); opacity: 0.25;
    -webkit-mask-image: linear-gradient(to top, #000, transparent 60%); mask-image: linear-gradient(to top, #000, transparent 60%);
  }

  .bold-line { font-family: "Montserrat", Arial, sans-serif; font-weight: 800; }
  .attractions-1 { top: 472px; font-size: 26px; line-height: 34px; }
  .attractions-2 { top: 504px; font-size: 30px; line-height: 38px; }
  .champagne { top: 538px; font-size: 29px; line-height: 38px; left: -10px; }
  .divider { font-weight: 400; padding: 0 6px; }

  .raffle { top: 595px; font-size: 17px; line-height: 19px; letter-spacing: 0.3px; }

  .prizes {
    position: absolute; left: 342px; top: 657px; width: 478px; height: 144px;
    background: var(--prize-blue); padding: 0 0 0 14px; font-size: 20px; letter-spacing: 0.9px;
    overflow: hidden;
  }
  .prizes li { list-style: none; height: 49px; line-height: 49px; white-space: nowrap; }
  .prizes .rank { font-family: "Montserrat", Arial, sans-serif; font-weight: 800; letter-spacing: 0; }
  .rank.first { color: var(--first-gold); }
  .rank.second { color: var(--second-silver); }
  .rank.third { color: var(--third-bronze); margin-left: -4px; }

  .drawing { top: 826px; font-size: 21px; line-height: 28px; left: -10px; }
</style>
</head>
<body>
<main class="flyer">
  <div class="date-banner">
    <p class="date">DECEMBER 31 @ 10 P.M.</p>
    <p class="venue">LOCATED AT COSTALUZ 72B</p>
  </div>

  <div class="title-glow"></div>
  <p class="center presenter">THE SOIREE FOUNDRY PRESENTS:</p>
  <h1 class="center headline"><span>BOLEN'S</span></h1>
  <p class="center annual"><span>3RD ANNUAL</span></p>
  <p class="center party-name">NEW YEARS EVE PARTY</p>
  <p class="center party-reflection" aria-hidden="true">NEW YEARS EVE PARTY</p>

  <p class="center bold-line attractions-1">DJ INSIDE <span class="divider">|</span> LIVE BAND OUTSIDE</p>
  <p class="center attractions-2">FOOD<span class="divider">|</span>BEVERAGES<span class="divider">|</span>BOUNCE HOUSE</p>
  <p class="center bold-line champagne">KING OF PEARLS CHAMPAGNE</p>

  <p class="center raffle">RAFFLE TICKETS WILL BE SOLD FOR A $20.00 DONATION AT<br>LOCATION OR CONTACT 63928/19476</p>

  <ul class="prizes">
    <li><span class="rank first">1ST</span> PRIZE 46 INCH VEXTRA LED TV</li>
    <li><span class="rank second">2ND</span> PRIZE 100 DOLLAR GIFT CERTIFICATE</li>
    <li><span class="rank third">3RD</span> PRIZE 50 DOLLAR GIFT CERTIFICATE</li>
  </ul>

  <p class="center bold-line drawing">DRAWING STARTS AT 1:30 AM</p>
</main>
</body>
</html>
```